Web Design for Cedarfield Yard Crew

Cedarfield Yard Crew needs the photoshop files for a simple, clean and professional web design. I need a home and subpage design, although they can be very similar. See pagestridelab.com for a desired layout, although I'd like to see more design than shown on that site. The goal of the site is to attract both lawn maintenance/landscape customers and build a partner network of consultants that serve the US market. The following are needed:

- home and subpage design
- page: Home, Services, Locations, Consultants, FAQ, Contact
- if subpages have header photo, need to include 5 different header photos for each page
- favicon
Updates

I'll award the design based on the homepage concept. The minor subpage changes and other elements can be worked out in the workroom stage. Thanks, Reid

Industry/Entity Type

It Professional

```html
<!DOCTYPE html>
<html lang="en">
<head>
<meta charset="utf-8">
<title>Cedarfield Yard Crew — Home</title>
<link href="https://fonts.googleapis.com/css2?family=Questrial&family=Open+Sans:wght@400;600&display=swap" rel="stylesheet">
<style>
:root{
  --green:#66ad3e;
  --green-dark:#579a32;
  --green-deep:#3f7a22;
  --ink:#3a3a3a;
  --grey:#808080;
  --rule:#d8d8d8;
  --footer:#333333;
  --white:#ffffff;
  --panel:rgba(18,38,10,.72);
}
*{margin:0;padding:0;box-sizing:border-box}
html,body{width:1200px;height:2848px;overflow:hidden;background:var(--white)}
body{position:relative;font-family:"Open Sans",Arial,sans-serif;color:var(--ink)}
.abs{position:absolute}
.display{font-family:"Questrial","Century Gothic",sans-serif}

/* top bar */
.topbar{left:0;top:0;width:1200px;height:49px;background:var(--green)}
.topbar .social{position:absolute;top:12px;display:flex;gap:10px;left:808px}
.dot{width:26px;height:26px;border-radius:50%;background:var(--white)}
.search{position:absolute;left:959px;top:11px;width:200px;height:27px;border-radius:14px;background:var(--white);font-size:12px;color:#999;padding:5px 14px}
.search svg{position:absolute;right:12px;top:7px}

/* header */
.header{left:0;top:49px;width:1200px;height:141px;background:var(--white)}
.brand{position:absolute;left:51px;top:33px;display:flex;align-items:center;gap:14px}
.brand .mark{width:54px;height:54px;border:3px solid #555;border-radius:8px}
.brand .name{font-family:"Questrial",sans-serif;font-size:30px;color:#555;line-height:1}
.nav{position:absolute;top:46px;left:0;width:1200px;font-family:"Questrial",sans-serif;font-size:15px;letter-spacing:1.5px;color:#444}
.nav a{position:absolute;color:inherit;text-decoration:none;line-height:30px}
.nav .active{background:#555;color:var(--white);border-radius:15px;padding:0 16px}

/* hero */
.hero{left:0;top:190px;width:1200px;height:507px;background:linear-gradient(135deg,#4f9a2c,#6fb845 45%,#3f8420)}
.quote-form{left:80px;top:281px;width:549px;height:266px;background:var(--panel);border-radius:0 0 14px 0}
.quote-form h2{height:42px;background:var(--green);color:var(--white);font-family:"Questrial",sans-serif;font-weight:400;font-size:25px;letter-spacing:1.5px;padding:6px 20px}
.quote-form p{color:var(--white);font-size:15px;padding:10px 26px 0}
.field{position:absolute;width:234px;height:36px;background:rgba(255,255,255,.35);color:var(--white);font-size:14px;padding:8px 12px;letter-spacing:.5px}
.submit{position:absolute;left:95px;top:195px;width:358px;height:36px;background:var(--green);color:var(--white);text-align:center;font-size:15px;letter-spacing:1px;line-height:36px}

/* section heads */
.rule{height:1px;background:var(--rule)}
.rule-dot{width:16px;height:16px;border-radius:50%;background:var(--green)}
.head{width:1200px;text-align:center;font-family:"Questrial",sans-serif;font-size:25px;letter-spacing:1.5px;color:#333}
.head em{font-style:normal;color:var(--green)}

/* welcome */
.video{left:85px;top:876px;width:447px;height:294px;border:1px solid #ccc;background:linear-gradient(160deg,#7cb84a,#4d8f2a 55%,#c9d9b8)}
.play{left:263px;top:976px;width:92px;height:92px;border-radius:50%;background:#333;opacity:.9}
.intro{left:594px;top:876px;width:540px;font-size:16px;line-height:26px;color:#444}
.ticks{left:598px;top:978px;width:540px;list-style:none;font-size:15.5px;line-height:25px;color:var(--grey)}
.ticks li{position:relative;padding-left:34px;margin-bottom:12px}
.ticks li svg{position:absolute;left:0;top:3px}

/* unique */
.unique{left:0;top:1248px;width:1200px;height:471px;background:var(--green);border-bottom:7px solid var(--green-deep)}
.unique .head{color:var(--white);top:40px;position:absolute}
.unique .rule{position:absolute;left:51px;top:93px;width:1097px;background:rgba(255,255,255,.3)}
.feature{position:absolute;top:118px;width:234px;height:304px;text-align:center;color:var(--white)}
.feature.is-active{background:var(--green-dark)}
.feature svg{margin-top:42px}
.feature h3{font-family:"Questrial",sans-serif;font-weight:400;font-size:19px;letter-spacing:1px;margin-top:20px}
.feature p{font-size:14px;line-height:17px;margin:12px auto 0;width:170px;font-weight:600}

/* consultants */
.avatar{border-radius:50%;border:5px solid #d0d0d0;background:radial-gradient(circle at 50% 40%,#9a9a9a,#444)}
.avatar.is-current{border-color:#cfcfcf;background:radial-gradient(circle at 50% 40%,#f0d8b0,#c49a6c)}
.arrow{top:1956px}
.person{left:0;top:2085px;width:1200px;text-align:center}
.person .who{font-family:"Questrial",sans-serif;font-size:16px;letter-spacing:1px;color:var(--green)}
.person .role{font-size:14px;color:var(--grey);letter-spacing:1px}
.testimonial{left:234px;top:2166px;width:784px;height:205px;border:1px solid #ddd;border-bottom:5px solid #cfcfcf;background:var(--white);box-shadow:0 2px 4px rgba(0,0,0,.05)}
.testimonial p{position:absolute;left:107px;top:40px;width:605px;font-size:16px;line-height:30px;color:#555}
.qmark{position:absolute;font-family:Georgia,serif;font-size:80px;color:#c8c8c8;line-height:1}

/* footer */
.footer{left:0;top:2470px;width:1200px;height:317px;background:var(--footer);color:var(--white)}
.col{position:absolute;top:58px}
.col h4{font-family:"Questrial",sans-serif;font-weight:400;font-size:18px;letter-spacing:1.5px;margin-bottom:18px}
.col a{display:block;color:#e8e8e8;font-size:13px;line-height:29.5px;text-decoration:none;padding-left:3px}
.foot-brand{position:absolute;left:794px;top:110px;display:flex;align-items:center;gap:14px}
.foot-brand .mark{width:50px;height:50px;border:3px solid #999;border-radius:8px}
.foot-brand .name{font-family:"Questrial",sans-serif;font-size:28px;color:#aaa}
.bottombar{left:0;top:2787px;width:1200px;height:61px;background:var(--green);color:var(--white);font-size:13px}
.bottombar span{position:absolute;left:116px;top:21px}
.bottombar .social{position:absolute;left:987px;top:16px;display:flex;gap:12px}
.bottombar .dot{width:30px;height:30px}
</style>
</head>
<body>

<div class="abs topbar">
  <div class="social"><span class="dot"></span><span class="dot"></span><span class="dot"></span><span class="dot"></span></div>
  <div class="search">Keyword Search...
    <svg width="14" height="14" viewBox="0 0 14 14"><circle cx="5.5" cy="5.5" r="4" fill="none" stroke="#888" stroke-width="2"/><line x1="8.5" y1="8.5" x2="13" y2="13" stroke="#888" stroke-width="2"/></svg>
  </div>
</div>

<header class="abs header">
  <div class="brand"><span class="mark"></span><span class="name">Cedarfield Yard Crew</span></div>
  <nav class="nav">
    <a class="active" style="left:441px">HOME</a>
    <a style="left:558px">SERVICES</a>
    <a style="left:678px">LOCATIONS</a>
    <a style="left:817px">CONSULTANTS</a>
    <a style="left:973px">FAQ</a>
    <a style="left:1054px">CONTACT US</a>
  </nav>
</header>

<div class="abs hero" role="img" aria-label="Top-down photo of a man pushing a lawn mower across a green lawn"></div>

<form class="abs quote-form">
  <h2>GET A FREE QUOTATION</h2>
  <p>Lorem ipsum dolor sit amet &nbsp;consectetur adipiscing elit.</p>
  <span class="field" style="left:26px;top:91px">Firstname</span>
  <span class="field" style="left:280px;top:91px">Email Address</span>
  <span class="field" style="left:26px;top:140px">Contact Number</span>
  <span class="field" style="left:280px;top:140px">Zip Code</span>
  <span class="submit">SUBMIT</span>
</form>

<section>
  <div class="abs head" style="left:0;top:730px;font-size:14px;color:#999;letter-spacing:1px">Welcome to</div>
  <h1 class="abs head" style="left:0;top:750px;font-weight:400">CEDARFIELD <em>YARD CREW</em></h1>
  <div class="abs rule" style="left:51px;top:811px;width:1097px"></div>
  <div class="abs rule-dot" style="left:592px;top:803px"></div>

  <div class="abs video" role="img" aria-label="Video still of a smiling gardener with arms crossed in front of hedges"></div>
  <svg class="abs" style="left:263px;top:976px" width="92" height="92" viewBox="0 0 92 92"><circle cx="46" cy="46" r="46" fill="#333" opacity=".9"/><path d="M36 28 L66 46 L36 64 Z" fill="#2aa3d8"/></svg>

  <p class="abs intro">Lorem ipsum dolor sit amet, consectetur adipiscing elit. Mat ecenas ullamcorper nisi non faucibus faucibus. Donec sapien magna, commodo at sodales pulvinar.</p>
  <ul class="abs ticks">
    <li><svg width="20" height="20" viewBox="0 0 20 20"><rect x="1" y="1" width="18" height="18" fill="none" stroke="#66ad3e" stroke-width="2"/><path d="M5 10 L9 14 L17 4" fill="none" stroke="#66ad3e" stroke-width="3"/></svg>Lorem ipsum dolor sit amet, consectetur adipiscing elit.</li>
    <li><svg width="20" height="20" viewBox="0 0 20 20"><rect x="1" y="1" width="18" height="18" fill="none" stroke="#66ad3e" stroke-width="2"/><path d="M5 10 L9 14 L17 4" fill="none" stroke="#66ad3e" stroke-width="3"/></svg>Commodo at magna donec et sapien.lorem ipsum dolor sit amet, consectetur adipiscing elit.</li>
    <li><svg width="20" height="20" viewBox="0 0 20 20"><rect x="1" y="1" width="18" height="18" fill="none" stroke="#66ad3e" stroke-width="2"/><path d="M5 10 L9 14 L17 4" fill="none" stroke="#66ad3e" stroke-width="3"/></svg>Maecenas ullamcorper nisi non faucibus faucibus. Donec sapien magna, commodo at sodales pulvinar.</li>
    <li><svg width="20" height="20" viewBox="0 0 20 20"><rect x="1" y="1" width="18" height="18" fill="none" stroke="#66ad3e" stroke-width="2"/><path d="M5 10 L9 14 L17 4" fill="none" stroke="#66ad3e" stroke-width="3"/></svg>Lorem ipsum dolor sit amet, consectetur adipiscing elit.</li>
  </ul>
</section>

<section class="abs unique">
  <h2 class="head" style="font-weight:400">WHAT'S UNIQUE ABOUT US?</h2>
  <div class="rule"></div>
  <div class="feature" style="left:187px">
    <svg width="104" height="104" viewBox="0 0 104 104"><circle cx="52" cy="52" r="52" fill="#fff"/><path d="M52 24 V52 L70 64" fill="none" stroke="#66ad3e" stroke-width="7" stroke-linecap="round"/><circle cx="52" cy="14" r="4" fill="#66ad3e"/><circle cx="14" cy="52" r="4" fill="#66ad3e"/><circle cx="90" cy="52" r="4" fill="#66ad3e"/><circle cx="52" cy="90" r="4" fill="#66ad3e"/></svg>
    <h3>Fast &amp; Efficient</h3>
    <p>Lorem ipsum dolor sit amet, consectetur adip iscing elit. Maec ullam</p>
  </div>
  <div class="feature is-active" style="left:484px">
    <svg width="104" height="104" viewBox="0 0 104 104"><circle cx="52" cy="52" r="52" fill="#fff"/><path d="M52 24 L60 43 L80 44 L64 57 L70 77 L52 66 L34 77 L40 57 L24 44 L44 43 Z" fill="#66ad3e"/></svg>
    <h3>Pro &amp; Friendly</h3>
    <p>Lorem ipsum dolor sit amet, consectetur adip iscing elit. Maec ullam</p>
  </div>
  <div class="feature" style="left:772px">
    <svg width="104" height="104" viewBox="0 0 104 104"><path d="M14 48 H30 V92 H14 Z M36 48 L52 14 C62 14 62 24 60 34 L58 42 H84 C92 42 94 50 90 56 C94 60 92 66 88 68 C91 72 89 78 84 80 C86 86 82 92 76 92 H36 Z" fill="none" stroke="#fff" stroke-width="7" stroke-linejoin="round"/></svg>
    <h3>Satisfying results</h3>
    <p>Lorem ipsum dolor sit amet, consectetur adip iscing elit. Maec ullam</p>
  </div>
</section>

<section>
  <h2 class="abs head" style="left:0;top:1767px;font-weight:400">OUR <em>CONSULTANTS</em></h2>
  <div class="abs rule" style="left:51px;top:1831px;width:1097px"></div>
  <div class="abs rule-dot" style="left:592px;top:1823px"></div>

  <svg class="abs arrow" style="left:117px" width="24" height="50" viewBox="0 0 24 50"><path d="M20 4 L4 25 L20 46" fill="none" stroke="#ccc" stroke-width="3"/></svg>
  <svg class="abs arrow" style="left:1109px" width="24" height="50" viewBox="0 0 24 50"><path d="M4 4 L20 25 L4 46" fill="none" stroke="#66ad3e" stroke-width="3"/></svg>

  <div class="abs avatar" role="img" aria-label="Consultant portrait" style="left:181px;top:1913px;width:136px;height:136px"></div>
  <div class="abs avatar" role="img" aria-label="Consultant portrait" style="left:363px;top:1913px;width:136px;height:136px"></div>
  <div class="abs avatar is-current" role="img" aria-label="Portrait of consultant Jane Doe" style="left:540px;top:1896px;width:170px;height:170px"></div>
  <div class="abs avatar" role="img" aria-label="Consultant portrait" style="left:754px;top:1913px;width:136px;height:136px"></div>
  <div class="abs avatar" role="img" aria-label="Consultant portrait" style="left:939px;top:1913px;width:136px;height:136px"></div>

  <div class="abs person"><div class="who">JANE DOE</div><div class="role">Job Position</div></div>

  <blockquote class="abs testimonial">
    <span class="qmark" style="left:30px;top:14px">&ldquo;</span>
    <p>Lorem ipsum dolor sit amet, consectetur adipiscing elit. Etiam dapibus, massa ac aliquam elementum, felis erat porta elit, id scelerisque ligula arcu nec metus. Sed interdum odio a eros dictum, in dignissim augue dictum. Morbi augue dui, venenatis et orci ut, sodales tristique metus.</p>
    <span class="qmark" style="left:716px;top:120px">&rdquo;</span>
  </blockquote>
  <svg class="abs" style="left:610px;top:2147px" width="40" height="21" viewBox="0 0 40 21"><path d="M0 20 L20 1 L40 20" fill="#fff" stroke="#ddd" stroke-width="1"/></svg>
</section>

<footer class="abs footer">
  <div class="col" style="left:120px"><h4>ABOUT US</h4><a>Bio</a><a>Client List</a><a>Contact Info</a></div>
  <div class="col" style="left:298px"><h4>SERVICES OFFERED</h4><a>Link goes here</a><a>Link goes here</a><a>Link goes here</a><a>Link goes here</a><a>Link goes here</a></div>
  <div class="col" style="left:545px"><h4>ADDITIONAL INFO</h4><a>Sitemap</a><a>FAQ</a><a>Privacy Policy</a><a>Terms &amp; Agreement</a></div>
  <div class="foot-brand"><span class="mark"></span><span class="name">Cedarfield Yard Crew</span></div>
</footer>

<div class="abs bottombar">
  <span>Cedarfield Yard Crew All Rights Reserved &reg; 2014</span>
  <div class="social"><span class="dot"></span><span class="dot"></span><span class="dot"></span></div>
</div>

</body>
</html>
```